Product presentation and placement brochure

I have cardiovascular exercise equipment (treadmill, bikes, eliptical trainers, etc.) that have a coin timers attached that allow use of this exercise equipment using coins. I want to market to apartment buildings, swimming pools, training gyms, etc. We want them to partner with us by allowing us to place our equipment in their locations. Their residents would get new equipment to use, they use a coin to get so much time. The apartment building doesn't pay anything precharge us workspace, but they will get a 10 - 20% of all the revenue that flows through the machines in their building.This brochure needs to clearly display our equipment, how the residents can use it, the ease of the relationship between us and the apartment building, and how they will make money with no investment and no commitment.I would, like the brochure to look artistic, not so mechanical.

Target Market(s)

Large apartment buildings, Public swimming pools, training studios, gyms, etc.

Font styles to use
Serif

Colors

Designer to choose colors to be used in the design.

Requirements
Must have
• The basic wording for the brochure. Must have English and Chinese.
• Vero Pulse Machine Brochure
• 維諾脈動健身器材指南
• We will pay YOU to let us provide YOU with commercial cardiovascular equipment.
• 我們付你錢來讓我們提供你有氧器材
• We supply cardio equipment to your residents at no cost to you. In fact, we will pay you! Please take a moment to look at our brochure and see how we can work with you and your homeowners association to bring the latest in fitness technology to your building, and we’ll pay you for it.
• 在不花費你任何金錢的情況下, 我們提供有氧器材給你的住戶。甚至我們付你錢!請看我們的手冊來了解我們如何能和你跟社區管理委員會合作, 把最新的健身器材介紹到你的大樓, 並且帶給你收益。
• Our machines are all equipped with patented coin operated technology. If your residents would like to have the luxury of quality exercise, they may insert dollars for minutes.
• 我們的器材皆具備專利通過投幣式設計。如果你的住戶想要享有高品質運動, 他們可以投幣來取得運動時間。
• By the 10th of every month, we will pay 15% of all revenue collected for the previous month, minus taxes, to you or your homeowners association, whichever you choose.
• 每個月10號, 我們將付你或社區管理委員會前一個月百分之十五不含稅的收入。
• Why it is so easy:
• 1. We provide the equipment at no cost to you.
• 2. We pay for shipping and installation.
• 3. Month-to-month agreement, no commitment from you.
• 4. Removal with 30 days notice, no questions asked.
• 5. We conduct all repairs and regular maintenance.
• 6. We will pay you from the revenue collected!
• 為什麼超簡單:
• 1. 不花你一毛錢, 器材我們提供。
• 2. 運送費跟安裝費, 全數我們支付。
• 3. 以一個月為一期, 不用長期保證。
• 4. 30天移出通知, 不需任何理由。
• 5. 所有器材維修, 我們負責。
• 6. 器材收益,我們分享!
• As easy as 1, 2, 3!
• 簡單有如1, 2, 3!
• STEP 1
• We have several different machine types that will motivate your residents to exercise:
• 1. Treadmill (photo and stats.)
• 2. Recumbent Bike (photo and stats.)
• 3. Regular Seated Bike (photo and stats.)
• 4. Elliptical trainer (photo and stats.)
• Replace old equipment, broken equipment, or just place new equipment next to your old equipment.
• 第一步
• 我們有多種有氧器材可讓住戶更有動力運動:
• 1. 跑步機
• 2. 臥式腳踏車
• 3. 直立式腳踏車
• 4. 橢圓機
• 替換原有老舊的運動器材, 或是直接放一台新的器材在原有器材的旁邊。
• After meeting with you and determining you and your residents needs, we will decide how many and of what types of equipment you would like in your exercise room.
• 在和你會面並且評估你和住戶的需求後, 我們會決定你想要的器材種類和數量。
• STEP 2
• We will deliver and install the equipment, in a suitable location that you choose. All at no cost to you!
• 第二步
• 我們將器材運送到你選擇的合適場所並安裝。不需任何費用!
• Step 3
• 第三步
• Make your residents healthy and happy by letting them use any of the equipment, for as long as they like, at their leisure.
• 住戶可盡情使用任何器材, 讓住戶健康又開心。
• Photo Steps on how to use equipment
• 0. 2. 3.
• We would be happy to answer any of your questions and give you a free consultation on how you can utilize this service to bring affordable fitness to your residents, while creating a revenue stream for you or your homeowners association.
• 我們很樂意回答任何問題並免費提供諮詢:如何有效利用此服務以帶給住戶能負擔的健身運動, 且同時創造收益給你或社區管理委員會。
• For more Information, please:
• visit our website at:
• call:
• Email:
• 更多資訊請:
• 拜訪我們的網站:
• 電話聯絡:
• 傳送電子郵件:
• Quentin Hale
• Marisol Tevet
• Vero Pulse Fitness
• Manager of Marketing and English Translation
• Ph: +17605550187
• LINE ID: driftingotter
• Email: drifting-otter@mailvoro.com
Nice to have
• I would like it to be have a high tech artsy feel. I don't want the haredline industrial.

```html
<!DOCTYPE html>
<html lang="en">
<head>
<meta charset="utf-8">
<title>Vero Pulse Machine Brochure</title>
<link href="https://fonts.googleapis.com/css2?family=Montserrat:wght@500;700;800;900&family=Open+Sans:wght@400;600&family=Noto+Sans+TC:wght@400;700&display=swap" rel="stylesheet">
<style>
:root{
  --yellow:#f3e600;
  --black:#151515;
  --ink:#3a3a3a;
  --grey:#8a8a8a;
  --paper:#ffffff;
  --stage:#ececec;
}
*{box-sizing:border-box;margin:0;padding:0}
html,body{width:739px;height:1200px;overflow:hidden;background:var(--stage)}
body{position:relative;font-family:"Open Sans","Noto Sans TC",sans-serif;color:var(--ink)}
.page{position:absolute;background:var(--paper);overflow:hidden;box-shadow:0 2px 10px rgba(0,0,0,.12)}
.page svg.shapes{position:absolute;inset:0;width:100%;height:100%}
.photo{position:absolute}
.headline{font-family:"Montserrat",sans-serif;font-weight:900;text-transform:uppercase;line-height:.95}
.small{font-size:5.6px;line-height:1.45}

/* back cover */
.back-cover{left:26px;top:40px;width:330px;height:466px}
.contact-title{position:absolute;left:26px;top:40px;color:var(--yellow);font-size:18px}
.contact-list{position:absolute;left:26px;top:74px;width:180px;list-style:none;color:#fff}
.contact-list li{display:flex;align-items:center;gap:7px;font-size:6.4px;margin-bottom:8px}
.contact-list .dot{width:11px;height:11px;border-radius:50%;background:var(--yellow);flex:none;display:flex;align-items:center;justify-content:center}
.contact-list strong{font-family:"Montserrat",sans-serif;font-weight:700;font-size:7px;display:block}
.consult{position:absolute;left:26px;top:200px;width:150px;color:#ddd}
.back-social{position:absolute;left:26px;top:236px;display:flex;gap:5px}
.back-social span{width:9px;height:9px;border-radius:50%;background:var(--yellow)}

/* front cover */
.front-cover{left:383px;top:40px;width:330px;height:466px}
.brand{position:absolute;left:0;right:0;top:22px;display:flex;flex-direction:column;align-items:center;gap:4px}
.brand .mark{width:34px;height:34px;border-radius:50%;background:var(--black)}
.brand .name{font-family:"Montserrat",sans-serif;font-weight:700;font-size:7px;letter-spacing:1.5px;color:var(--black);text-transform:uppercase}
.cover-title{position:absolute;right:22px;top:350px;text-align:right;transform:rotate(-9deg);transform-origin:right center}
.cover-title .line1{color:var(--yellow);font-size:27px;-webkit-text-stroke:0}
.cover-title .line2{color:var(--black);font-size:30px}
.cover-title .zh{font-family:"Noto Sans TC",sans-serif;font-weight:700;font-size:8px;color:var(--ink);margin-top:4px}
.cover-web{position:absolute;left:20px;bottom:18px;font-size:5.5px;color:var(--grey)}

/* inner spread */
.inner{left:24px;top:566px;width:690px;height:488px}
.inner .fold{position:absolute;left:345px;top:0;width:1px;height:100%;background:rgba(0,0,0,.08)}
.intro{position:absolute;left:24px;top:30px;width:290px}
.intro p{margin-bottom:5px}
.easy-band{position:absolute;left:0;top:150px;width:200px;height:22px;background:var(--black);clip-path:polygon(0 0,100% 0,90% 100%,0 100%)}
.easy-band h2{color:var(--yellow);font-size:10px;padding:6px 0 0 24px}
.easy-list{position:absolute;left:24px;top:184px;width:300px;display:grid;grid-template-columns:1fr 1fr;gap:7px 14px;list-style:none}
.easy-list li{display:flex;align-items:center;gap:6px;font-size:5.6px;line-height:1.35}
.hex{width:14px;height:14px;flex:none;background:var(--black);clip-path:polygon(25% 0,75% 0,100% 50%,75% 100%,25% 100%,0 50%);color:var(--yellow);font-family:"Montserrat",sans-serif;font-weight:800;font-size:7px;display:flex;align-items:center;justify-content:center}
.step-tag{position:absolute;background:var(--black);color:var(--yellow);font-family:"Montserrat",sans-serif;font-weight:800;font-size:7.5px;padding:3px 10px 3px 8px;clip-path:polygon(0 0,100% 0,88% 100%,0 100%)}
.step-text{position:absolute;width:290px}
.machines{position:absolute;left:371px;top:168px;display:flex;gap:6px}
.machines .photo{position:relative;width:94px;height:62px}
.easy123{position:absolute;left:371px;top:44px;font-size:11px;color:var(--black)}
</style>
</head>
<body>

<!-- Back cover -->
<section class="page back-cover" aria-label="Back cover">
  <svg class="shapes" viewBox="0 0 330 466" aria-hidden="true">
    <polygon points="0,0 330,0 330,40 225,270 0,300" fill="#151515"/>
    <g stroke="#ffffff" stroke-opacity=".06" stroke-width="8">
      <line x1="210" y1="0" x2="330" y2="120"/><line x1="240" y1="0" x2="330" y2="90"/><line x1="270" y1="0" x2="330" y2="60"/>
    </g>
    <polygon points="225,270 330,40 330,70 238,275" fill="#f3e600"/>
    <polygon points="0,300 225,270 215,284 0,314" fill="#f3e600"/>
  </svg>
  <div class="photo" role="img" aria-label="Black and white photo of cardio machines in a gym" style="left:0;top:318px;width:330px;height:148px;background:linear-gradient(160deg,#9a9a9a,#4a4a4a 60%,#2b2b2b);clip-path:polygon(0 0,100% 0,100% 100%,0 100%)"></div>
  <svg class="shapes" viewBox="0 0 330 466" aria-hidden="true">
    <polygon points="250,466 300,380 312,380 262,466" fill="#f3e600"/>
    <polygon points="275,466 325,380 330,380 330,392 287,466" fill="#f3e600"/>
  </svg>
  <h2 class="headline contact-title">Contact Us</h2>
  <ul class="contact-list">
    <li><span class="dot"></span><span><strong>Quentin Hale</strong>Marisol Tevet · Vero Pulse Fitness</span></li>
    <li><span class="dot"></span><span>Manager of Marketing and English Translation</span></li>
    <li><span class="dot"></span><span>Ph: +17605550187</span></li>
    <li><span class="dot"></span><span>LINE ID: driftingotter</span></li>
    <li><span class="dot"></span><span>Email: drifting-otter@mailvoro.com</span></li>
    <li><span class="dot"></span><span>www.veropulsefitness.com</span></li>
  </ul>
  <p class="small consult">For more Information, please visit our website, call or email us. 更多資訊請拜訪我們的網站。</p>
  <div class="back-social" aria-hidden="true"><span></span><span></span><span></span></div>
</section>

<!-- Front cover -->
<section class="page front-cover" aria-label="Front cover">
  <div class="brand"><span class="mark"></span><span class="name">Vero Pulse Fitness</span></div>
  <svg class="shapes" viewBox="0 0 330 466" aria-hidden="true">
    <polygon points="230,90 330,70 330,150" fill="#f3e600"/>
    <polygon points="40,150 330,96 330,112 30,164" fill="#151515"/>
  </svg>
  <div class="photo" role="img" aria-label="Photo of treadmills lined up in a bright fitness room" style="left:0;top:0;width:330px;height:466px;background:linear-gradient(135deg,#c9c9c9,#6d6d6d 45%,#d8cf3a 85%);clip-path:polygon(12% 36%,100% 24%,100% 68%,0 82%,0 40%)"></div>
  <svg class="shapes" viewBox="0 0 330 466" aria-hidden="true">
    <polygon points="0,382 330,317 330,334 0,398" fill="#f3e600"/>
    <polygon points="0,404 330,340 330,346 0,410" fill="#151515"/>
    <polygon points="330,420 330,466 250,466" fill="#151515"/>
    <polygon points="330,440 330,466 285,466" fill="#f3e600"/>
  </svg>
  <div class="cover-title">
    <h1 class="headline"><span class="line1">Vero Pulse</span><br><span class="line2">Machine</span></h1>
    <p class="zh">維諾脈動健身器材指南</p>
  </div>
  <p class="cover-web">www.veropulsefitness.com</p>
</section>

<!-- Inner spread -->
<section class="page inner" aria-label="Inner spread">
  <svg class="shapes" viewBox="0 0 690 488" aria-hidden="true">
    <polygon points="600,0 690,0 690,70" fill="#f3e600"/>
    <polygon points="560,0 590,0 690,80 690,100" fill="#151515"/>
    <polygon points="0,340 345,300 345,312 0,352" fill="#f3e600"/>
  </svg>
  <div class="fold"></div>

  <div class="intro small">
    <p><b>We will pay YOU to let us provide YOU with commercial cardiovascular equipment.</b> 我們付你錢來讓我們提供你有氧器材</p>
    <p>We supply cardio equipment to your residents at no cost to you. In fact, we will pay you! Please take a moment to look at our brochure and see how we can work with you and your homeowners association to bring the latest in fitness technology to your building, and we’ll pay you for it.</p>
    <p>Our machines are all equipped with patented coin operated technology. If your residents would like to have the luxury of quality exercise, they may insert dollars for minutes.</p>
    <p>By the 10th of every month, we will pay 15% of all revenue collected for the previous month, minus taxes, to you or your homeowners association, whichever you choose.</p>
  </div>

  <div class="easy-band"><h2 class="headline">Why it is so easy:</h2></div>
  <ol class="easy-list">
    <li><span class="hex">1</span>We provide the equipment at no cost to you.</li>
    <li><span class="hex">2</span>We pay for shipping and installation.</li>
    <li><span class="hex">3</span>Month-to-month agreement, no commitment from you.</li>
    <li><span class="hex">4</span>Removal with 30 days notice, no questions asked.</li>
    <li><span class="hex">5</span>We conduct all repairs and regular maintenance.</li>
    <li><span class="hex">6</span>We will pay you from the revenue collected!</li>
  </ol>
  <div class="photo" role="img" aria-label="Photo of a resident exercising on a cardio machine" style="left:0;top:318px;width:345px;height:170px;background:linear-gradient(150deg,#d9cf45,#8d8a55 45%,#4a4a44);clip-path:polygon(0 22%,100% 0,100% 100%,0 100%)"></div>

  <h2 class="headline easy123">As easy as 1, 2, 3!</h2>
  <span class="step-tag" style="left:371px;top:70px">STEP 1</span>
  <p class="step-text small" style="left:371px;top:88px">We have several different machine types that will motivate your residents to exercise: 1. Treadmill 2. Recumbent Bike 3. Regular Seated Bike 4. Elliptical trainer. Replace old equipment, broken equipment, or just place new equipment next to your old equipment. After meeting with you and determining you and your residents needs, we will decide how many and of what types of equipment you would like.</p>
  <div class="machines">
    <div class="photo" role="img" aria-label="Photo of a treadmill" style="background:linear-gradient(135deg,#b9c4cf,#4f5a66)"></div>
    <div class="photo" role="img" aria-label="Photo of a recumbent bike" style="background:linear-gradient(135deg,#c2cbd6,#56606b)"></div>
    <div class="photo" role="img" aria-label="Photo of an elliptical trainer" style="background:linear-gradient(135deg,#bcc6d0,#525c67)"></div>
  </div>
  <span class="step-tag" style="left:371px;top:244px">STEP 2</span>
  <p class="step-text small" style="left:371px;top:262px">We will deliver and install the equipment, in a suitable location that you choose. All at no cost to you!</p>
  <span class="step-tag" style="left:371px;top:290px">STEP 3</span>
  <p class="step-text small" style="left:371px;top:308px">Make your residents healthy and happy by letting them use any of the equipment, for as long as they like, at their leisure.</p>
  <div class="photo" role="img" aria-label="Photo of a gym room with cardio equipment" style="left:345px;top:360px;width:345px;height:128px;background:linear-gradient(160deg,#e2d84a,#7c7a4e 50%,#3d3d38);clip-path:polygon(0 20%,100% 0,100% 100%,0 100%)"></div>
</section>

</body>
</html>
```